Business Association needs street banner design promoting business district.

We are a business association that manages a commercial district of small family owned businesses. We would like to install banners (30 inches wide by 60 inches long) on street lights. The banners will include our logo and the name of the sponsor (we will need a space for the sponsor information). We will also need a space to include a photo of the sponsoring business (this space needs to be large). The banners are intended to promote the local small businesses. For more information on our organization, our web site is www.larkmoorba.org.

Target Market(s)

Member businesses and customers.

Industry/Entity Type

Small Business

Font styles to use
Sans Serif

Requirements
Must have
• Any images or type must be large enough for pedestrians to read from a distance. Brights colors. No copy 4 inches from top or bottom (the banners will be folded and sewn). These banners will be installed on street lights (see example image in files). Please design banner in Adobe Illustrator.
• Text on banner: "Welcome to Larkmoor!" Please include logo on banner.

```html
<!DOCTYPE html>
<html lang="en">
<head>
<meta charset="utf-8">
<title>Larkmoor Street Banner</title>
<link href="https://fonts.googleapis.com/css2?family=Audiowide&family=Libre+Baskerville:ital@1&family=Open+Sans:wght@400;600&display=swap" rel="stylesheet">
<style>
  :root {
    --page: #eef0f2;
    --black: #050505;
    --red: #b3181c;
    --white: #ffffff;
    --ink: #1a1a1a;
    --sky: #7fa9c9;
    --sea: #2f6f9a;
    --city: #6b6258;
  }
  * { margin: 0; padding: 0; box-sizing: border-box; }
  html, body {
    width: 1056px; height: 1200px; overflow: hidden;
    background: var(--page);
  }
  .banner {
    position: absolute; left: 248px; top: 40px;
    width: 560px; height: 1120px;
    display: flex; flex-direction: column;
    background: var(--white);
    box-shadow: 0 2px 10px rgba(0,0,0,.18);
  }
  .hem { height: 75px; background: var(--black); flex: none; }
  .headline {
    height: 80px; flex: none; background: var(--red);
    display: flex; align-items: center; justify-content: center;
    color: var(--white);
    font-family: "Audiowide", sans-serif;
    font-size: 30px; font-style: italic; letter-spacing: 1px;
  }
  .sponsor-photo {
    height: 600px; flex: none;
    background: linear-gradient(180deg, var(--sky) 0%, var(--sea) 16%, #8a8f93 24%, var(--city) 60%, #3f3a35 100%);
  }
  .rule { height: 14px; flex: none; background: var(--red); }
  .credits { flex: 1; display: flex; align-items: center; }
  .association {
    width: 50%; padding-left: 30px;
    font-family: "Open Sans", sans-serif; color: var(--ink);
    display: flex; flex-direction: column; align-items: flex-start;
  }
  .association-mark {
    width: 60px; height: 60px; border-radius: 50%;
    background: var(--red); margin: 0 0 14px 68px;
  }
  .association-name {
    font-weight: 600; font-size: 17px; line-height: 1.15; text-transform: uppercase;
  }
  .association-web { font-size: 15px; margin-top: 4px; }
  .divider { width: 4px; height: 170px; background: var(--red); }
  .sponsor {
    flex: 1; padding-left: 24px;
    font-family: "Open Sans", sans-serif; color: var(--ink);
  }
  .sponsor-name {
    font-family: "Libre Baskerville", serif; font-style: italic;
    font-size: 44px; line-height: 1.1; margin-bottom: 14px;
  }
  .sponsor-contact { font-size: 15px; line-height: 1.35; }
</style>
</head>
<body>
  <div class="banner">
    <div class="hem"></div>
    <div class="headline">Welcome to Larkmoor!</div>
    <div class="sponsor-photo" role="img" aria-label="Photo of the sponsoring business: aerial view of downtown towers by the lake"></div>
    <div class="rule"></div>
    <div class="credits">
      <div class="association">
        <div class="association-mark"></div>
        <div class="association-name">Larkmoor<br>Business Association</div>
        <div class="association-web">www.larkmoorba.org.</div>
      </div>
      <div class="divider"></div>
      <div class="sponsor">
        <div class="sponsor-name">Martin Hale</div>
        <div class="sponsor-contact">Main Street,<br>number, City Name<br>(Country)123-456-789.</div>
      </div>
    </div>
    <div class="hem"></div>
  </div>
</body>
</html>
```